International Honeymoon Tour Operator needs Business Card

We need to design a business card including our new logo for a new tour operator called Marisol Thorne Getaways. We would like to also include the text 'Personal Tailor-Made Honeymoons for our Guests at a Lower Cost'. Please Include the following details as well; 'Website: www.marisolthornegetaways.co.uk'; 'E-mail: felix@marisolthornegetaways.co.uk'; 'Mobile: 07914263058'. We would like the design to be compatible with the logo and text. The final design should communicate professionalism, modern and ethical.

We want to business card to be double sided.

We would like to be able to easily adjust the e-mail address and contact number in the future for other employees either through you or ourselves.

Target Market(s)

Brides and grooms aged 18-35 predominantly.

Industry/Entity Type

Business

Colors

Designer to choose colors to be used in the design.

Requirements
Must have
• Logo
Requested Text
Double sided
Nice to have
• Additional colour
The wow factor
Should not have
• Images of currency

```html
<!DOCTYPE html>
<html lang="en">
<head>
<meta charset="utf-8">
<title>Marisol Thorne Getaways – Business Card</title>
<link href="https://fonts.googleapis.com/css2?family=Anton&family=Libre+Baskerville:wght@700&family=Poppins:wght@400&display=swap" rel="stylesheet">
<style>
  :root {
    --page-bg: #e9e6df;
    --card-bg: #ffffff;
    --green: #2f8a3e;
    --green-light: #d9eed3;
    --green-pale: #f3f9f0;
    --teal: #3f8f86;
    --ink: #111111;
  }
  html, body {
    margin: 0;
    width: 1200px;
    height: 833px;
    overflow: hidden;
    background: var(--page-bg);
  }
  .card {
    position: absolute;
    left: 50px;
    top: 106px;
    width: 1100px;
    height: 620px;
    background: var(--card-bg);
    box-shadow: 0 6px 22px rgba(0,0,0,0.18);
    overflow: hidden;
  }
  .card-frame {
    position: absolute;
    inset: 10px;
    border: 5px solid var(--green);
  }
  .card-frame::after {
    content: "";
    position: absolute;
    inset: 6px;
    border: 1.5px solid var(--green);
  }
  .swirl-area {
    position: absolute;
    right: 30px;
    top: 90px;
    width: 230px;
    height: 500px;
    background: linear-gradient(160deg, var(--green-pale), var(--green-light) 60%, var(--green-pale));
    opacity: 0.6;
    border-radius: 10px;
  }
  .tagline {
    position: absolute;
    top: 40px;
    left: 0;
    right: 0;
    text-align: center;
    margin: 0;
    font-family: "Libre Baskerville", serif;
    font-weight: 700;
    font-variant: small-caps;
    font-size: 29px;
    letter-spacing: 0.3px;
    color: var(--ink);
    white-space: nowrap;
  }
  .brand-mark {
    position: absolute;
    left: 170px;
    top: 100px;
    width: 160px;
    height: 160px;
    border-radius: 50%;
    background: var(--teal);
  }
  .call-us {
    position: absolute;
    left: 560px;
    top: 120px;
    margin: 0;
    font-family: "Anton", sans-serif;
    font-size: 42px;
    line-height: 1.2;
    color: var(--green);
    white-space: nowrap;
  }
  .brand-name {
    position: absolute;
    left: 50px;
    top: 285px;
    margin: 0;
    font-family: "Poppins", sans-serif;
    font-weight: 400;
    font-size: 62px;
    line-height: 1.05;
    color: var(--teal);
  }
  .contact-list {
    position: absolute;
    left: 300px;
    top: 462px;
    margin: 0;
    padding: 0;
    list-style: none;
    font-family: "Poppins", sans-serif;
    font-size: 27px;
    line-height: 1.3;
    color: var(--ink);
  }
  .contact-list li {
    margin-bottom: 34px;
    white-space: nowrap;
  }
  .contact-list li::before {
    content: "";
    display: inline-block;
    width: 10px;
    height: 10px;
    border-radius: 50%;
    background: var(--ink);
    margin-right: 10px;
    vertical-align: middle;
  }
</style>
</head>
<body>
  <section class="card" aria-label="Marisol Thorne Getaways business card">
    <div class="swirl-area" role="img" aria-label="Decorative green swirls and leaves"></div>
    <div class="card-frame"></div>
    <p class="tagline">Personal Tailor-Made Honeymoons For Guests At A Lower Cost</p>
    <span class="brand-mark"></span>
    <p class="call-us">Call Us Today: 07914263058</p>
    <p class="brand-name">Marisol Thorne<br>Getaways</p>
    <ul class="contact-list">
      <li>Website: www.marisolthornegetaways.co.uk</li>
      <li>Email : felix@marisolthornegetaways.co.uk</li>
    </ul>
  </section>
</body>
</html>
```